Marlow Estates Business Card and Email Signature Design

I am a Homevant and need a business card design with my head shot picture and logo and contact information that can be prepared to be used on my email signature as well. I would like my head shot image background to match the background of the business card. So in other words the background of my head shot should be transparent. I would like the Homevant Logo on there and also PRX and Fair Dwelling Logo. My email address is: ted@marlowestates.example, Phone Number is: 555-014-7391, website: www.marlowestates.example Address: 48207 Quillfern Court Ashbury, KS 66099
I also need just the head shot photo with white background in a JPEG file as well so I can upload that picture to my Jobtrellis and Nestavo profiles.

```html
<!DOCTYPE html>
<html lang="en">
<head>
<meta charset="utf-8">
<title>Marlow Estates Business Card</title>
<link rel="stylesheet" href="https://fonts.googleapis.com/css2?family=Montserrat:wght@500;600&family=Work+Sans:wght@400&display=swap">
<style>
  :root {
    --bg: #2f2927;
    --card: #1c1c1d;
    --card-edge: #15517e;
    --silver: #b9b9bb;
    --silver-soft: #8e8e90;
    --accent: #1f74b8;
    --ink: #f2f2f2;
    --rule: #e6e6e6;
  }
  * { margin: 0; padding: 0; box-sizing: border-box; }
  html, body { width: 1200px; height: 715px; overflow: hidden; }
  body {
    background: var(--bg);
    position: relative;
    font-family: "Work Sans", sans-serif;
  }
  .card {
    position: absolute;
    top: 203px;
    width: 540px;
    height: 309px;
    background: var(--card);
    border-radius: 6px;
  }
  .card-front { left: 40px; border-bottom: 4px solid var(--card-edge); }
  .card-back { left: 620px; }

  .brand {
    position: absolute;
    left: 0; right: 0; top: 110px;
    text-align: center;
  }
  .brand-name {
    font-family: "Montserrat", sans-serif;
    font-weight: 600;
    font-size: 34px;
    letter-spacing: 1px;
    color: var(--silver);
    display: inline-flex;
    align-items: center;
    gap: 14px;
  }
  .brand-dot {
    width: 26px; height: 26px;
    border-radius: 50%;
    background: var(--silver);
  }
  .brand-tagline {
    margin-top: 6px;
    font-family: "Montserrat", sans-serif;
    font-weight: 500;
    font-size: 14px;
    letter-spacing: 4px;
    color: var(--silver-soft);
  }

  .headshot {
    position: absolute;
    left: 48px; top: 78px;
    width: 150px; height: 150px;
    border-radius: 50%;
    border: 3px solid var(--rule);
    background: radial-gradient(circle at 50% 40%, #6b5a50 0%, #3a3a44 55%, #22232a 100%);
  }
  .divider {
    position: absolute;
    left: 245px; top: 82px;
    width: 2px; height: 145px;
    background: var(--rule);
  }
  .details {
    position: absolute;
    left: 275px; top: 92px;
    color: var(--ink);
    font-size: 13px;
    line-height: 1.45;
  }
  .agent-name {
    font-family: "Montserrat", sans-serif;
    font-weight: 600;
    font-size: 25px;
    color: var(--accent);
    letter-spacing: 0.5px;
    line-height: 1.1;
  }
  .agent-role { margin-bottom: 6px; }
  .contact-line { display: flex; align-items: center; gap: 7px; }
  .contact-line svg { width: 10px; height: 10px; fill: var(--accent); flex: none; }
</style>
</head>
<body>
  <section class="card card-front">
    <div class="brand">
      <div class="brand-name"><span class="brand-dot"></span>MARLOW ESTATES</div>
      <div class="brand-tagline">REAL ESTATE SERVICES</div>
    </div>
  </section>

  <section class="card card-back">
    <div class="headshot" role="img" aria-label="Agent head shot in a dark suit"></div>
    <div class="divider"></div>
    <div class="details">
      <div class="agent-name">OWEN HARTLEY</div>
      <div class="agent-role">Homevant</div>
      <div>48207 Quillfern Court</div>
      <div>Ashbury, KS 66099</div>
      <div class="contact-line">
        <svg viewBox="0 0 10 10"><path d="M2 0.5 L3.6 0.5 L4.3 2.8 L3.2 3.7 Q4.2 5.9 6.3 6.8 L7.2 5.7 L9.5 6.4 L9.5 8 Q9.5 9.5 8 9.5 Q0.5 9 0.5 2 Q0.5 0.5 2 0.5 Z"/></svg>
        <span>555-014-7391</span>
      </div>
      <div class="contact-line">
        <svg viewBox="0 0 10 10"><path d="M0.5 2 H9.5 V8 H0.5 Z M0.5 2 L5 5.5 L9.5 2" fill="none" stroke="#1f74b8" stroke-width="1.2"/></svg>
        <span>ted@marlowestates.example</span>
      </div>
      <div class="contact-line">
        <svg viewBox="0 0 10 10"><circle cx="5" cy="5" r="4.5"/></svg>
        <span>www.marlowestates.example</span>
      </div>
    </div>
  </section>
</body>
</html>
```